???KT580

I have created a design to some extent.
This time the body is beige.
I am attaching some rough drawings.

Can you make the logo a little nicer?
Can you fix it like the style of the attached logo?
We want the letters on the side to be gold leaf style. We would like to have a round logo on the rear side.
HINOKI Samples that you want the logo to look like the logo of the company. These should not be used in the design.

```html
<!DOCTYPE html>
<html lang="en">
<head>
<meta charset="utf-8">
<title>HINOKIHOUSE Master Carpenter – KT580 van wrap sides</title>
<link rel="stylesheet" href="https://fonts.googleapis.com/css2?family=Montserrat:wght@800&family=Oswald:wght@500&family=Noto+Sans+JP:wght@900&display=swap">
<style>
  :root {
    --beige: #ecd7a9;
    --navy: #163a55;
    --paper: #ffffff;
    --pale: #f4efe4;
  }
  * { margin: 0; padding: 0; box-sizing: border-box; }
  html, body { width: 1200px; height: 1200px; overflow: hidden; background: var(--paper); }
  .canvas { position: relative; width: 1200px; height: 1200px; }
  .wrap-side {
    position: absolute; left: 50px; width: 1100px; height: 440px;
    background: var(--beige); overflow: hidden; border-radius: 28px 60px 18px 18px;
  }
  .wrap-side--rear-band { top: 70px; }
  .wrap-side--front-logo { top: 640px; }
  .wrap-side svg.graphics { position: absolute; inset: 0; }
  .txt { position: absolute; color: var(--navy); white-space: nowrap; line-height: 1; }
  .brand-name { font-family: "Montserrat", sans-serif; font-weight: 800; font-size: 58px; letter-spacing: 1px; }
  .trade { font-family: "Oswald", sans-serif; font-weight: 500; font-size: 46px; letter-spacing: 0.5px; }
  .slogan { font-family: "Oswald", sans-serif; font-weight: 500; font-size: 30px; }
  .slogan--stacked { text-align: right; line-height: 1.15; }
  .call-strip {
    font-family: "Oswald", sans-serif; font-weight: 500; font-size: 24px;
    color: var(--beige); letter-spacing: 3px;
  }
  .call-strip .number { font-size: 30px; letter-spacing: 2px; margin-left: 10px; }
  .call-label { font-family: "Oswald", sans-serif; font-weight: 500; font-size: 26px; color: var(--pale); letter-spacing: 1px; }
  .phone { font-family: "Oswald", sans-serif; font-weight: 500; font-size: 36px; letter-spacing: 1.5px; }
  .shop-jp { font-family: "Noto Sans JP", sans-serif; font-weight: 900; font-size: 32px; letter-spacing: 3px; }
  .mark-name { font-family: "Montserrat", sans-serif; font-weight: 800; fill: var(--navy); }
</style>
</head>
<body>
<main class="canvas">

  <section class="wrap-side wrap-side--rear-band">
    <svg class="graphics" width="1100" height="440" viewBox="0 0 1100 440">
      <path class="rear-band" d="M0 0 H70 V330 Q70 362 110 362 H960 V404 H0 Z" fill="var(--navy)"/>
      <circle cx="225" cy="185" r="138" fill="var(--beige)" stroke="var(--navy)" stroke-width="18"/>
      <text class="mark-name" x="225" y="199" font-size="40" text-anchor="middle">HINOKI</text>
    </svg>
    <p class="txt slogan slogan--stacked" style="left:390px; top:70px; width:170px;">BUILD<br>AS YOU WISH</p>
    <h1 class="txt brand-name" style="left:405px; top:200px;">HINOKIHOUSE</h1>
    <p class="txt trade" style="left:440px; top:270px;">MASTER CARPENTER</p>
    <p class="txt call-strip" style="left:335px; top:368px;">PLEASE CALL ME<span class="number">090-4821-3907</span></p>
  </section>

  <section class="wrap-side wrap-side--front-logo">
    <svg class="graphics" width="1100" height="440" viewBox="0 0 1100 440">
      <circle cx="760" cy="265" r="148" fill="var(--beige)" stroke="var(--navy)" stroke-width="18"/>
      <text class="mark-name" x="760" y="279" font-size="40" text-anchor="middle">HINOKI</text>
    </svg>
    <h2 class="txt brand-name" style="left:50px; top:40px;">HINOKIHOUSE</h2>
    <p class="txt trade" style="left:105px; top:115px;">MASTER CARPENTER</p>
    <p class="txt shop-jp" style="left:165px; top:176px;">森の木リホーム</p>
    <p class="txt slogan" style="left:55px; top:262px; font-size:28px;">BUILD AS YOU WISH</p>
    <p class="txt call-label" style="left:320px; top:262px;">PLEASE CALL ME</p>
    <p class="txt phone" style="left:275px; top:302px;">090-4821-3907</p>
  </section>

</main>
</body>
</html>
```